2 page Web Site Design (Coded), simple, not picky

I need a web portal for a PPC marketing business. I have the logo, some imagery, and some websites to base the design on.

***Background***
The name of the business is "Quiet Harbor Outreach Partners" or QHOP. We provide listings in a searchable database for Dental Sleep Medicine doctors. These are doctors who treat snoring/sleep apnea/and CPAP users with oral appliances. Client doctors will have their own "landing page website" where PPC prospects land from the PPC campaigns. Logos for supporting/landing page websites have been uploaded.
***End Background***

THIS website (for you to design) is to introduce doctors to the concept and detail the services. i.e. PPC campaign management services, listing on a national database of Dental Sleep Medicine practitioners, and a fully featured website dedicated to Snoring, Sleep Apnea, and CPAP Alternative treatment (those websites are "Farewell-Rumble.com", "Farewell-NightPause.com", and ""Farewell-MaskFree.com")

SEM websites whose look I enjoy are:

http://www.brivolta.com/marketing-services/pay-per-click/

http://www.quellandrift.com/welcome/pay-per-click-services/

http://www.tarnolux4co.com/marketing-services/paid-search-management/

The main colors are Red, White, & Blue. Red and blue used mostly for accents/emphasis.

The main/index page's purpose is to, as best possible, convey the idea of SEM campaign management with supporting websites being their best option for internet marketing!
The secondary page is just a slightly modified layout where details can be explained.

Target Market(s)

Dentists who practice Dental Sleep Medicine (see www.pqwrl.org)

Industry/Entity Type

Marketing

Requirements
Must have
• -Sign-up form for the generation of leads... Simple script that sends E-mail is fine... Doctor's Name, Business Name, Business Address, E-mail address, phone #.

-Graphics that will clearly describe the services being provided.

```html
<!DOCTYPE html>
<html lang="en">
<head>
<meta charset="utf-8">
<title>Quiet Harbor Outreach Partners</title>
<link href="https://fonts.googleapis.com/css2?family=Arimo:wght@400;700&family=Roboto+Condensed:wght@400;700&display=swap" rel="stylesheet">
<style>
:root{
  --red:#b8282f;
  --red-dark:#98161c;
  --blue:#163a80;
  --blue-dark:#0f2b66;
  --navy:#1b2f6b;
  --text:#333;
  --page:#ececec;
  --white:#fff;
}
*{box-sizing:border-box;margin:0;padding:0}
html,body{width:1063px;height:1200px;overflow:hidden}
body{position:relative;background:linear-gradient(#f4f4f4,var(--page));font-family:"Arimo",Arial,sans-serif;color:var(--text);font-size:11px}
.abs{position:absolute}
.header{left:0;top:0;width:1063px;height:80px;background:linear-gradient(#fff,#f2f2f2)}
.logo-card{left:120px;top:0;width:275px;height:137px;background:linear-gradient(#fff,#e9e9e9);border:1px solid #ccc;border-top:none;border-radius:0 0 6px 6px;box-shadow:0 3px 8px rgba(0,0,0,.25);z-index:3;display:flex;flex-direction:column;align-items:center;justify-content:center;gap:6px}
.logo-name{display:flex;align-items:center;gap:10px;font-weight:700;font-size:38px;color:var(--red)}
.logo-mark{width:34px;height:34px;border-radius:50%;background:var(--navy)}
.logo-tag{font-weight:700;font-size:12px;color:var(--red)}
.nav{left:520px;top:29px;display:flex;align-items:center;font-size:13px}
.nav a{color:var(--blue);text-decoration:none}
.nav .active{background:linear-gradient(#3d6dc4,#173f8c);color:#fff;border-radius:12px;padding:4px 12px;border:1px solid #0d2a66}
.nav .about{margin-left:66px}.nav .services{margin-left:78px}.nav .contact{margin-left:60px}
.hero{left:0;top:80px;width:1063px;height:381px;background:radial-gradient(ellipse at 62% 35%,#e2b5a8 0%,#b98275 28%,#6f3a34 55%,#3b2624 80%)}
.hero-fade{left:0;top:400px;width:1063px;height:61px;background:linear-gradient(rgba(236,236,236,0),rgba(236,236,236,.4))}
.promo{left:122px;top:184px;width:275px;height:313px;background:linear-gradient(#c9343b,var(--red-dark));border:1px solid #e06a6f;border-radius:4px;color:#fff;box-shadow:0 2px 6px rgba(0,0,0,.35);z-index:2}
.card-head{text-align:center;padding:13px 0 15px;border-bottom:1px solid rgba(255,255,255,.18)}
.card-head h2{font-family:"Roboto Condensed",Arial,sans-serif;font-weight:400;font-size:22px}
.card-head p{font-size:12px;margin-top:2px}
.card-body{padding:12px 16px 0 14px;font-size:10.4px;line-height:1.2}
.card-list{list-style:none;margin-top:11px}
.card-list li{position:relative;padding-left:26px;margin-bottom:10px}
.card-list li::before{content:"";position:absolute;left:12px;top:4px;border-left:4px solid #fff;border-top:3px solid transparent;border-bottom:3px solid transparent}
.btn-more{position:absolute;right:17px;bottom:12px;width:88px;height:22px;border-radius:11px;background:linear-gradient(#4d7fd6,#173f8c);border:1px solid #0d2a66;color:#fff;font-size:12px;text-align:center;line-height:20px}
.shadow-ellipse{height:12px;border-radius:50%;background:radial-gradient(ellipse,rgba(0,0,0,.22),rgba(0,0,0,0) 70%)}
.headline{left:409px;top:288px;width:532px;height:155px;background:rgba(255,240,240,.78);border:1px solid #fff;border-radius:3px;overflow:hidden}
.headline-art{position:absolute;right:0;top:0;width:200px;height:155px;background:linear-gradient(100deg,rgba(255,255,255,0) 10%,rgba(255,255,255,.55) 100%)}
.headline h1{position:absolute;left:18px;top:10px;font-weight:400;font-size:26px;color:var(--navy);line-height:1.18}
.headline h1 strong{font-weight:700;font-size:23.5px}
.headline p{position:absolute;left:33px;top:92px;width:350px;font-size:12px;line-height:1.3;color:#222}
.headline p::before{content:"";position:absolute;left:-15px;top:4px;width:6px;height:6px;border-left:2px solid var(--red);border-bottom:2px solid var(--red)}
.content{left:106px;top:484px;width:849px;height:660px;background:#fff;border:1px solid #ddd;border-radius:3px}
.pcc{left:122px;top:531px;width:275px;height:259px;background:linear-gradient(var(--blue),var(--blue-dark));border-radius:3px;color:#fff}
.pcc .card-head{padding:13px 0 14px}
.pcc .card-list{margin-top:0}
.pcc .card-list li{margin-bottom:13px;font-size:10px}
.signup{left:122px;top:812px;width:275px;height:286px;background:#fff;border:1px solid #ddd;border-radius:3px}
.signup h2{font-family:"Roboto Condensed",Arial,sans-serif;font-weight:400;font-size:22px;text-align:center;padding:14px 0 16px;border-bottom:1px solid #e2e2e2;color:#222}
.field{position:absolute;left:18px;font-size:11px;color:#333}
.input{position:absolute;left:125px;width:135px;height:18px;border:1px solid #bbb;border-radius:3px;background:linear-gradient(#d9d9d9,#f4f4f4)}
.submit{position:absolute;left:125px;top:251px;width:82px;height:24px;border-radius:12px;background:linear-gradient(#cf3a40,#a3181e);border:1px solid #7d0f13;color:#fff;font-size:13px;text-align:center;line-height:22px}
.main{left:420px;top:526px;width:512px;font-size:11px;line-height:1.45;color:#444}
.main h1{font-family:"Roboto Condensed",Arial,sans-serif;font-weight:400;font-size:22px;color:#222;padding-bottom:8px;border-bottom:1px solid #ddd;margin-bottom:10px}
.main h2{font-size:16px;color:var(--red);margin:18px 0 16px}
.main h3{font-size:16px;color:var(--blue);margin:0 0 16px}
.shots{display:flex;gap:11px;margin:16px 0 24px}
.shot{width:251px;height:228px;border:1px solid #ccc;background:linear-gradient(#fff,#f6f1c8 60%,#fbf9ea)}
.bullets{list-style:none;margin-top:14px}
.bullets li{position:relative;padding-left:12px;margin-bottom:1px;color:#333}
.bullets li::before{content:"";position:absolute;left:0;top:5px;border-left:4px solid var(--red);border-top:3px solid transparent;border-bottom:3px solid transparent}
.read-more{font-weight:700;color:var(--blue);font-size:10px;margin-top:3px}
.footer{left:108px;top:1160px;font-size:9px;color:#555;line-height:1.3}
</style>
</head>
<body>
<div class="abs header"></div>
<div class="abs logo-card">
  <div class="logo-name"><span class="logo-mark"></span>QHOP</div>
  <div class="logo-tag">Quiet Harbor Outreach Partners</div>
</div>
<nav class="abs nav">
  <a class="active" href="#">Landing Page</a>
  <a class="about" href="#">About</a>
  <a class="services" href="#">Services</a>
  <a class="contact" href="#">Contact</a>
</nav>

<div class="abs hero" role="img" aria-label="Soft-focus photo of a patient resting during oral appliance sleep therapy"></div>
<div class="abs hero-fade"></div>

<div class="abs headline">
  <div class="headline-art" role="img" aria-label="Growth graphic suggesting rising results"></div>
  <h1>Customized internet marketing solution<br><strong>specially designed for OSB Therapists!</strong></h1>
  <p>Will drive customers to your practice with PPC Search engine Marketing and then educate them about the unique benefits inherent to OAT therapy with a dedicated website .</p>
</div>

<div class="abs content"></div>

<section class="abs promo">
  <div class="card-head"><h2>Search Engine Marketing</h2><p>Online marketing strategy</p></div>
  <div class="card-body">
    <p>Search engine marketing is an online marketing strategy that aims to increase qualified visitor traffic to your website by positioning your advertisements at the top and right side of “natural” and “organic” search result pages</p>
    <ul class="card-list">
      <li>You only pay when someone clicks on one of your advertisements.</li>
      <li>It is estimated that pay per click ads receive around 30% of all clicks on search engines.</li>
      <li>Seekwell Ads, Yonder Search Marketing and Northgate AdHub are pay per click advertising platforms.</li>
    </ul>
  </div>
  <div class="btn-more">More</div>
</section>
<div class="abs shadow-ellipse" style="left:146px;top:500px;width:222px"></div>

<section class="abs pcc">
  <div class="card-head"><h2>Pay Per Click</h2><p>Search Engine Marketing Campaign Managment.</p></div>
  <div class="card-body">
    <ul class="card-list">
      <li>We set up and manage your search engine marketing campaigns for you.</li>
      <li>You only pay when visitors click on your ad and visit your website.</li>
      <li>We design your ad campaign to optimize ad click conversion rates.</li>
      <li>We send you regular advertising effectiveness monitoring, and analysis reports so you can determine your return-on-investment and adjust your budget accordingly.</li>
    </ul>
  </div>
</section>

<section class="abs signup">
  <h2>Signup Today!</h2>
  <span class="field" style="top:78px">Doctor's Name</span><span class="input" style="top:70px"></span>
  <span class="field" style="top:105px">Business Name</span><span class="input" style="top:98px"></span>
  <span class="field" style="top:133px">Business Address</span><span class="input" style="top:125px;height:57px"></span>
  <span class="field" style="top:207px;left:21px">E-mail address</span><span class="input" style="top:200px"></span>
  <span class="field" style="top:234px">Phone.No</span><span class="input" style="top:227px"></span>
  <div class="submit">Submit</div>
</section>
<div class="abs shadow-ellipse" style="left:146px;top:1096px;width:222px"></div>

<main class="abs main">
  <h1>Welcome to Quiet Harbor Outreach Partners</h1>
  <p>will drive customers to your practice with PPC Search engine Marketing and then educate them about the unique benefits inherent to OAT therapy with a dedicated website .</p>
  <h2>What is Search Engine Marketing?</h2>
  <p>Search engine marketing is an online marketing strategy that aims to increase qualified visitor traffic to your website by positioning your advertisements at the top and right side of “natural” and “organic” search result pages [descriptions below].</p>
  <div class="shots">
    <div class="shot" role="img" aria-label="Search results page with pay per click ads highlighted"></div>
    <div class="shot" role="img" aria-label="Search results page with natural search results highlighted"></div>
  </div>
  <h3>Search Engine Marketing(Pay Per Click)</h3>
  <p>Paid search results, called “Pay Per Click” (PPC) advertising, promote websites in “Sponsored” section of search results.</p>
  <ul class="bullets">
    <li>You only pay when someone clicks on one of your advertisements.</li>
    <li>It is estimated that pay per click ads receive around 30% of all clicks on search engines.</li>
    <li>Seekwell Ads, Yonder Search Marketing and Northgate AdHub are pay per click advertising platforms.</li>
  </ul>
  <div class="read-more">Read More...</div>
</main>

<footer class="abs footer">Copyrights@Quiet Harbor Outreach Partners.com<br>All rights reserved.</footer>
</body>
</html>
```